Bref créative
QVEN
Maple Growth Allies for Youth
I need single sided standard sized Business Card [3.5" x 2"]
Use the Logo font or others - Open to ideas....
Professional
Marissa Holden, M.S., CCC/SLP
Owner of SproutWell Therapy
4816 Fenwick Parkway, Suite 215
Dallas, Texas 75219
mholden@sproutwelltherapy.example
www.qven.example
Looking for professional and clean.

```html
<!DOCTYPE html>
<html lang="en">
<head>
<meta charset="utf-8">
<title>QVEN Business Card</title>
<link href="https://fonts.googleapis.com/css2?family=Open+Sans:ital,wght@0,400;0,600;0,700;0,800;1,400&display=swap" rel="stylesheet">
<style>
  :root {
    --page-bg: #e9e7e3;
    --card-white: #ffffff;
    --brand-blue: #2b3a93;
    --brand-blue-dark: #1f2b78;
    --brand-red: #d4262f;
    --ink-light: #ffffff;
  }
  * { margin: 0; padding: 0; box-sizing: border-box; }
  html, body {
    width: 1200px; height: 780px; overflow: hidden;
    background: var(--page-bg);
    font-family: "Open Sans", Arial, sans-serif;
  }
  .business-card {
    position: absolute; left: 75px; top: 90px;
    width: 1050px; height: 600px;
    border-radius: 34px; overflow: hidden;
    background: var(--card-white);
    box-shadow: 0 6px 18px rgba(0,0,0,0.18);
  }
  .card-shapes { position: absolute; inset: 0; }
  .brand-mark {
    position: absolute; left: 0; right: 0; top: 110px;
    text-align: center;
  }
  .brand-name {
    display: inline-flex; align-items: center; gap: 18px;
    font-size: 128px; font-weight: 800; letter-spacing: 4px;
    color: var(--brand-blue); line-height: 1;
  }
  .brand-dot {
    width: 34px; height: 34px; border-radius: 50%;
    background: var(--brand-red);
  }
  .brand-tagline {
    margin-top: 14px;
    font-size: 24px; font-weight: 700; letter-spacing: 1.5px;
    text-transform: uppercase; color: var(--brand-blue);
  }
  .contact-person {
    position: absolute; left: 58px; top: 400px;
    color: var(--ink-light);
  }
  .person-name { font-size: 30px; font-weight: 700; }
  .person-role { font-size: 22px; font-style: italic; margin-top: 2px; }
  .person-address { font-size: 22px; margin-top: 26px; line-height: 1.4; }
  .column-divider {
    position: absolute; left: 528px; top: 400px;
    width: 2px; height: 160px; background: var(--ink-light); opacity: 0.85;
  }
  .contact-lines {
    position: absolute; left: 552px; top: 398px;
    list-style: none; color: var(--ink-light);
    font-size: 21px;
  }
  .contact-lines li {
    display: flex; align-items: center; gap: 12px; height: 40px;
  }
  .contact-icon { width: 24px; height: 24px; flex: none; }
</style>
</head>
<body>
  <div class="business-card">
    <svg class="card-shapes" viewBox="0 0 1050 600" width="1050" height="600" aria-hidden="true">
      <path d="M0 340 C 300 300, 650 365, 1050 262 L1050 285 C 650 390, 300 330, 0 362 Z" fill="var(--brand-red)"/>
      <path d="M0 372 C 300 338, 650 398, 1050 298 L1050 600 L0 600 Z" fill="var(--brand-blue)"/>
    </svg>

    <div class="brand-mark">
      <div class="brand-name"><span>QVEN</span><span class="brand-dot"></span></div>
      <div class="brand-tagline">Maple Growth Allies for Youth</div>
    </div>

    <div class="contact-person">
      <p class="person-name">Marissa Holden, M.S., CCC/SLP</p>
      <p class="person-role">Owner of SproutWell Therapy</p>
      <p class="person-address">4816 Fenwick Parkway, Suite 215<br>Dallas, Texas 75219</p>
    </div>

    <div class="column-divider"></div>

    <ul class="contact-lines">
      <li>
        <svg class="contact-icon" viewBox="0 0 24 24"><path fill="#fff" d="M6.6 10.8a15.5 15.5 0 0 0 6.6 6.6l2.2-2.2c.3-.3.7-.4 1-.2 1.1.4 2.3.6 3.6.6.6 0 1 .4 1 1V20c0 .6-.4 1-1 1A17 17 0 0 1 3 4c0-.6.4-1 1-1h3.5c.6 0 1 .4 1 1 0 1.3.2 2.5.6 3.6.1.3 0 .7-.2 1z"/></svg>
        <span>(214) 555-0148</span>
      </li>
      <li>
        <svg class="contact-icon" viewBox="0 0 24 24"><rect x="6" y="3" width="12" height="6" fill="#fff"/><rect x="3" y="10" width="18" height="8" rx="2" fill="#fff"/><rect x="7" y="15" width="10" height="6" fill="#fff" stroke="var(--brand-blue)" stroke-width="1.5"/></svg>
        <span>(214) 555-0173</span>
      </li>
      <li>
        <svg class="contact-icon" viewBox="0 0 24 24"><circle cx="12" cy="12" r="4" fill="none" stroke="#fff" stroke-width="2.2"/><path d="M16 8v5a2.5 2.5 0 0 0 5 0v-1a9 9 0 1 0-3.5 7.1" fill="none" stroke="#fff" stroke-width="2.2"/></svg>
        <span>mholden@sproutwelltherapy.example</span>
      </li>
      <li>
        <svg class="contact-icon" viewBox="0 0 24 24"><circle cx="12" cy="12" r="9.5" fill="none" stroke="#fff" stroke-width="2"/><path d="M2.5 12h19M12 2.5c3 3 3 16 0 19M12 2.5c-3 3-3 16 0 19" fill="none" stroke="#fff" stroke-width="1.6"/></svg>
        <span>www.qven.example</span>
      </li>
    </ul>
  </div>
</body>
</html>
```